Bref créative
Sun Path & Oak Hill
Business Cards & Stationary
Use same font as used in my logo
marla teswick
director of operations
p o box 87
larkmont, ar 72915
spoh@postvale.com
501(c)3

```html
<!DOCTYPE html>
<html lang="en">
<head>
<meta charset="utf-8">
<title>Sun Path &amp; Oak Hill – Business Card</title>
<link rel="stylesheet" href="https://fonts.googleapis.com/css2?family=Cabin:wght@400;500&family=Annie+Use+Your+Telescope&display=swap">
<style>
  :root {
    --paper: #ffffff;
    --ink: #2f2f2f;
    --ink-soft: #555555;
    --pink: #e5378a;
    --pink-light: #f6c4da;
  }
  html, body {
    margin: 0;
    padding: 0;
    overflow: hidden;
    background: var(--paper);
  }
  .card {
    position: relative;
    width: 1200px;
    height: 686px;
    background: var(--paper);
    font-family: "Cabin", "Gill Sans", sans-serif;
    color: var(--ink);
    overflow: hidden;
  }
  .brand {
    position: absolute;
    left: 110px;
    top: 76px;
    display: flex;
    align-items: center;
    gap: 20px;
  }
  .brand-dot {
    width: 44px;
    height: 44px;
    border-radius: 50%;
    background: var(--pink-light);
    flex: none;
  }
  .brand-name {
    margin: 0;
    font-family: "Cabin", "Gill Sans", sans-serif;
    font-weight: 500;
    font-size: 58px;
    line-height: 1.08;
    color: var(--ink);
  }
  .tagline {
    position: absolute;
    left: 53px;
    top: 252px;
    margin: 0;
    font-size: 27px;
    letter-spacing: 6px;
    color: var(--pink);
    text-transform: uppercase;
  }
  .license {
    position: absolute;
    left: 53px;
    top: 296px;
    margin: 0;
    font-size: 13px;
    color: var(--ink-soft);
  }
  .person {
    position: absolute;
    left: 46px;
    top: 526px;
  }
  .person-name {
    margin: 0;
    font-family: "Annie Use Your Telescope", cursive;
    font-weight: 400;
    font-size: 58px;
    line-height: 1;
    color: var(--pink);
  }
  .person-role {
    margin: 6px 0 0 4px;
    font-size: 28px;
    letter-spacing: 0.5px;
    color: var(--ink);
    text-transform: uppercase;
  }
  .contact {
    position: absolute;
    left: 809px;
    top: 470px;
    margin: 0;
    display: grid;
    grid-template-columns: 36px auto;
    row-gap: 8px;
    font-size: 31px;
    line-height: 1.3;
    color: var(--ink);
  }
  .contact dt { color: var(--pink); }
  .contact dd { margin: 0; }
  .footer-band {
    position: absolute;
    left: 0;
    bottom: 0;
    width: 1200px;
    height: 24px;
    background: var(--pink-light);
  }
</style>
</head>
<body>
  <main class="card">
    <header class="brand">
      <span class="brand-dot" aria-hidden="true"></span>
      <h1 class="brand-name">Sun Path &amp;<br>Oak Hill</h1>
    </header>
    <p class="tagline">Walk together</p>
    <p class="license">License No. 501(c)3</p>

    <section class="person">
      <h2 class="person-name">marla teswick</h2>
      <p class="person-role">Director of Operations</p>
    </section>

    <dl class="contact">
      <dt>T:</dt><dd>390 555 0163</dd>
      <dt>E:</dt><dd>spoh@postvale.com</dd>
      <dt>A:</dt><dd>PO Box 87 Larkmont,<br>ar 72915</dd>
    </dl>

    <div class="footer-band" aria-hidden="true"></div>
  </main>
</body>
</html>
```